Letterhead design x 2, follower page, with compliments slip and envelope design X 2

Design letterhead x 2, follower page, with compliments slip and envelope x 2 for Harbourline Trade Advisors, a business broking company. Using the colours of the existing logo and a white background for a clean, sophisticated look.

Target Market(s)

Family Business owners and regular business owners looking to buy or sell their business, or improve the value of their business.

Font styles to use
Sans Serif

Requirements
Must have
• Letterhead design 1 - Additional logos for Torvald Trade Exchange, QLMR and HCX to be included in a small size somewhere on the page. Torvald Trade Exchange logo only to have the wording 'Powered By' alongside. Please do not distort the size of the logos.
Letterhead design 2 - Additional logos for QLMR and HCX to be included in a small size somewhere on the page. This design will not include the Torvald Trade Exchange logo or the words 'Powered By'. Please do not distort the size of the logos.
Envelope design 1 - Please include an address window
Envelope design 2 - Do not include an address window

```html
<!DOCTYPE html>
<html lang="en">
<head>
<meta charset="utf-8">
<title>Harbourline Trade Advisors – DL Envelope</title>
<link rel="stylesheet" href="https://fonts.googleapis.com/css2?family=Roboto:wght@400;500&display=swap">
<style>
  :root {
    --backdrop: #f1f2f3;
    --paper: #ffffff;
    --brand-orange: #f15a24;
    --brand-grey: #9a9ea3;
    --text-grey: #58595b;
  }
  html, body {
    margin: 0;
    padding: 0;
    width: 1200px;
    height: 1200px;
    overflow: hidden;
    background: var(--backdrop);
    font-family: "Roboto", Arial, sans-serif;
  }
  .envelope {
    position: absolute;
    left: 74px;
    top: 364px;
    width: 1052px;
    height: 472px;
    background: var(--paper);
    box-shadow: 0 1px 3px rgba(0,0,0,0.12);
  }
  .brand {
    position: absolute;
    left: 58px;
    top: 46px;
    display: flex;
    align-items: center;
    gap: 18px;
  }
  .brand-ring {
    width: 88px;
    height: 88px;
    border: 5px solid var(--brand-grey);
    border-radius: 50%;
    box-sizing: border-box;
  }
  .brand-name {
    margin: 0;
    color: var(--brand-orange);
    font-weight: 500;
    font-size: 27px;
    line-height: 28px;
    letter-spacing: -0.2px;
  }
  .sender {
    position: absolute;
    left: 60px;
    top: 352px;
    margin: 0;
    font-style: normal;
    color: var(--text-grey);
    font-size: 17px;
    line-height: 26px;
  }
  .sender-line {
    display: flex;
    align-items: center;
    gap: 6px;
  }
  .icon {
    width: 15px;
    height: 15px;
    fill: var(--brand-orange);
    flex: none;
  }
  .contact-item + .icon { margin-left: 4px; }
</style>
</head>
<body>
  <section class="envelope">
    <div class="brand">
      <div class="brand-ring"></div>
      <p class="brand-name">Harbourline<br>Trade<br>Advisors</p>
    </div>

    <address class="sender">
      <div class="sender-line">Suite 4, 18 Wharf Row, Fremantle Quay, WA, 6160</div>
      <div class="sender-line">
        <svg class="icon" viewBox="0 0 24 24" aria-hidden="true"><path d="M6.6 10.8a15.1 15.1 0 0 0 6.6 6.6l2.2-2.2a1 1 0 0 1 1-.25 11.4 11.4 0 0 0 3.6.57 1 1 0 0 1 1 1V20a1 1 0 0 1-1 1A17 17 0 0 1 3 4a1 1 0 0 1 1-1h3.5a1 1 0 0 1 1 1c0 1.25.2 2.45.57 3.57a1 1 0 0 1-.25 1z"/></svg>
        <span class="contact-item">08 5550 1842</span>
        <svg class="icon" viewBox="0 0 24 24" aria-hidden="true"><path d="M2 8c2-3 6-4 10-4s8 1 10 4l-3 3-4-2V7H9v2l-4 2zM5 13h14l1 7H4z"/></svg>
        <span class="contact-item">0491 570 316</span>
        <svg class="icon" viewBox="0 0 24 24" aria-hidden="true"><path d="M2 5h20v14H2zm2 2v.5l8 5 8-5V7z"/></svg>
        <span class="contact-item">ellis@harbourlinetrade.com.au</span>
      </div>
      <div class="sender-line">www.harbourlinetrade.com.au</div>
    </address>
  </section>
</body>
</html>
```